Buch-/E-Book-Cover im Bereich der Persönlichkeitsentwicklung
Vielen lieben Dank für die super Arbeit von Dir. Das Design ist klasse und die vielen Vorschläge waren auch super. Die komplette Zusammenarbeit verlief sehr professionell und Änderungswünsche wurden sehr schnell umgesetzt. Ich kann Dich voll und ganz weiterempfehlen.
Zielgruppe
Wir arbeiten in der Persönlichkeitsentwicklung für Jugendliche. Dabei spezialisieren wir uns auf den Altersbereich 12 - 17 Jahre. Unser Ziel ist es jungen Menschen zu zeigen, wie Sie zu sich selbst finden und ein glückliches sowie erfolgreiches Leben führen können.
Aufgabenstellung
- Das Design sollte für die Eltern von Teenagern und auch für die Teenager selbst ausgelegt werden. Das Buch ist für die Jugendlichen (Mädchen und Jungen im Alter zwischen 12 Jahren und 17 Jahren) gedacht, wird allerdings meist von deren Mütter gekauft.
- Der Name des Autors lautet: Jochen Brabeck
- Der Titel lautet: Junge Leute finden Mut und Richtung
- Der Untertitel lautet: Was Heranwachsende über eigene Stärken lernen
- Im Anhang befinden sich Designs, die ich gut finde (nur falls jemand weitere Ideen haben möchte)
- Format: 15,24 cm x 22,86 cm (6' x 9') [genaue Maße fürs Taschenbuch und Hardcover sind im Anhang (.zip Dateien)]
1. E-Book:
- Coverdateien sollten idealerweise 2 560 Pixel hoch und 1 600 Pixel breit sein. Zur Gewährleistung der bestmöglichen Qualität (insbesondere auf HD-Geräten) sollte das Bild mindestens 2 500 Pixel hoch sein.
- Format: TIFF (.tif/.tiff) oder JPEG (.jpeg/.jpg)
- DPI: 72 dpi
- Größe: Ihr Coverbild muss kleiner als 50 MB sein.
Hinweis: Vermeiden Sie es, Ihre Dateien zu komprimieren. Dies kann die Qualität Ihres Covers auf Lesegeräten beeinträchtigen. Das beste Ergebnis erzielen Sie mit Bildern, die eine Mindestauflösung von 300 ppi (Pixels per Inch) haben.
- Rahmen: Coverbilder mit weißem oder sehr hellem Hintergrund heben sich kaum vom weißen Hintergrund ab. Fügen Sie einen dünnen Rahmen (3–4 Pixel) in Mittelgrau hinzu, um die Ränder des Covers besser sichtbar zu machen.
2. + 3. Taschenbuch/Hardcover [genaue Maße fürs Taschenbuch und Hardcover sind im Anhang (.zip Dateien)] :
- Dateityp: Das Cover muss als einzelne PDF-Datei vorliegen und die hintere Coverseite, den Buchrücken und die vordere Coverseite als einzelnes Bild enthalten.
- Dateigröße: Coverdateien, die größer als 650 MB sind, können nicht konvertiert werden. Die Datei sollte maximal 40 MB groß sein, da sich bei großen Dateien der Druck verlangsamt.
- Die gen..

```html
<!DOCTYPE html>
<html lang="de">
<head>
<meta charset="utf-8">
<title>Junge Leute finden Mut und Richtung – Buchcover</title>
<link rel="stylesheet" href="https://fonts.googleapis.com/css2?family=Cabin+Sketch:wght@700&family=Amatic+SC:wght@700&family=Roboto+Condensed:wght@700&family=Gochi+Hand&display=swap">
<style>
  :root {
    --page: #ffffff;
    --sky-top: #4d88c6;
    --sky-mid: #7fb3dc;
    --sky-low: #a9d2ea;
    --rock-light: #8f8a7d;
    --rock-dark: #4f4a40;
    --ink: #1c1a18;
    --chalk: #ffffff;
    --frame: #222222;
  }
  * { margin: 0; padding: 0; box-sizing: border-box; }
  html, body {
    width: 1200px; height: 1200px; overflow: hidden;
    background: var(--page);
  }
  .cover {
    position: absolute;
    left: 242px; top: 61px;
    width: 715px; height: 1077px;
    border: 1px solid var(--frame);
    overflow: hidden;
    background:
      linear-gradient(200deg, var(--sky-top) 0%, var(--sky-mid) 45%, var(--sky-low) 80%, #b9dbe9 100%);
  }
  .author {
    position: absolute; top: 36px; left: 0; width: 100%;
    text-align: center;
    font-family: "Roboto Condensed", sans-serif;
    font-weight: 700; font-size: 27px; letter-spacing: 1.5px;
    color: var(--ink);
  }
  .title { color: var(--chalk); }
  .title span { position: absolute; white-space: nowrap; line-height: 1; }
  .title .big {
    font-family: "Cabin Sketch", cursive;
    font-weight: 700;
  }
  .title .small {
    font-family: "Gochi Hand", cursive;
    font-size: 48px;
  }
  .line-1 { left: 100px; top: 140px; font-size: 100px; letter-spacing: -1px; transform: rotate(-2deg); }
  .line-2 { left: 300px; top: 270px; }
  .line-3 { left: 76px; top: 300px; font-size: 210px; letter-spacing: -4px; }
  .line-4 { left: 468px; top: 422px; }
  .line-5 { left: 265px; top: 500px; font-size: 100px; letter-spacing: -2px; transform: rotate(-1.5deg); }
  .subtitle {
    position: absolute; right: 462px; top: 598px;
    text-align: right;
    font-family: "Amatic SC", cursive;
    font-weight: 700; font-size: 36px; line-height: 1.1;
    color: var(--ink);
    white-space: nowrap;
    transform: rotate(-1.5deg);
  }
  .group-photo {
    position: absolute;
    left: 66px; right: 0; bottom: 0; height: 370px;
    border-top-left-radius: 60px 220px;
    background:
      linear-gradient(180deg, rgba(169,210,234,0) 0%, rgba(143,138,125,0.55) 35%, var(--rock-light) 62%, var(--rock-dark) 100%);
  }
</style>
</head>
<body>
  <main class="cover">
    <p class="author">JOCHEN BRABECK</p>
    <h1 class="title">
      <span class="big line-1">Junge Leute</span>
      <span class="small line-2">finden</span>
      <span class="big line-3">Mut</span>
      <span class="small line-4">und</span>
      <span class="big line-5">Richtung</span>
    </h1>
    <p class="subtitle">WAS HERANWACHSENDE<br>ÜBER EIGENE STÄRKEN<br>LERNEN</p>
    <div class="group-photo" role="img" aria-label="Foto: vier Jugendliche sitzen im Sonnenlicht auf einer alten Felsmauer vor blauem Himmel und unterhalten sich"></div>
  </main>
</body>
</html>
```